Modernize Website: marcusvellory.com

I am a novelist with an older-generation website at: marcusvellory.com.

I am hoping to refresh this outdated website with a new, responsive redesign. I would prefer to host the code myself, and edit using Adobe Dreamweaver. So I’m not looking to use a hosted site builder like Qop. Nor am I looking to use a CMS like Pagecraft.

In order to simplify the old site, there are a number of sections I’ll be looking to remove during this redesign. These are shown in the "MV Site Redesign" attachment. I can also provide imagery for new content (another book series in addition to the existing one), as well as higher-resolution imagery (if needed) of the old content.

Happy to answer any further questions.
Updates

I've uploaded a ZIP file containing high-res artwork associated with the new trilogy of books.

Target Market(s)

Readers of epic fantasy novels such as H.P.L. Arkwood's THE KEEPER OF THE VALES, Harold P.J. Quimby's A TALE OF ASH AND STORM, Dennis Corwel's THE GATE OF DAWNS, or Colin Varnes's CROWN OF VELDRIMOR.

Industry/Entity Type

Entertainment

Coding

Coded - Design and coding required

Number of Pages Required

5+ page

Font styles to use
Serif
Decorative

Colors

Designer to choose colors to be used in the design.

Requirements
Must have
• I'm looking for a responsive design that displays nicely on both mobile and desktop devices. Existing site contains multiple pages, but these can obviously be combined into fewer pages (or even one) by divisions such as tabs, sections, and/or modal windows. See marcusvellory.com for current content and "MV Site Redesign" attachment for content to be removed at this time.
Nice to have
• The ability to fulfill orders of autographed books directly from the website. I currently use Coinlane to do this, but it would be nice to incorporate a more comprehensive merchant service at a reasonable rate.
Should not have
• I'd like to host and control the site code myself. So please don't use a hosted web builder like Qop, or a cloud-based CMS like Pagecraft.

```html
<!DOCTYPE html>
<html lang="en">
<head>
<meta charset="utf-8">
<title>Marcus Vellory – Books</title>
<link href="https://fonts.googleapis.com/css2?family=Cinzel+Decorative:wght@400;700&display=swap" rel="stylesheet">
<style>
  :root {
    --bg: #000000;
    --ink: #ffffff;
    --line: #d9d9d9;
    --accent: #c4142c;
    --accent-bright: #d61a33;
  }
  * { box-sizing: border-box; margin: 0; padding: 0; }
  html, body {
    width: 1200px; height: 588px; overflow: hidden;
    background: var(--bg); color: var(--ink);
    font-family: "Cinzel Decorative", serif;
  }
  .site { position: relative; width: 1200px; height: 588px; overflow: hidden; }

  .topbar { position: absolute; left: 0; top: 0; width: 1200px; height: 40px; }
  .brand { position: absolute; left: 2px; top: 3px; font-size: 27px; line-height: 34px; letter-spacing: -0.5px; }
  .nav { position: absolute; top: 0; left: 0; height: 40px; width: 100%; }
  .nav-item { position: absolute; top: 11px; display: flex; align-items: center; font-size: 14px; line-height: 18px; }
  .nav-item svg { width: 20px; height: 20px; fill: var(--ink); margin-right: 12px; }
  .nav-item .caret { width: 14px; height: 14px; margin: 0 0 0 14px; }
  .nav-home { left: 686px; }
  .nav-novels { left: 789px; }
  .nav-world { left: 900px; }
  .nav-author { left: 1046px; }

  .search-label {
    position: absolute; left: 13px; top: 60px; font-size: 13px; line-height: 16px;
  }
  .search-rule { position: absolute; left: 13px; top: 88px; width: 1158px; height: 1px; background: var(--line); }

  .book-list {
    position: absolute; left: 13px; top: 104px; width: 1158px; height: 520px;
    border: 1px solid var(--line); list-style: none;
  }
  .book { position: relative; height: 167px; border-bottom: 1px solid var(--line); }
  .cover { position: absolute; left: 8px; top: 27px; width: 87px; height: 132px; }
  .cover-1 { background: linear-gradient(160deg, #6e6f86 0%, #4b4560 45%, #8a7a8c 70%, #3b4d62 100%); }
  .cover-2 { background: linear-gradient(180deg, #b8402a 0%, #d8622a 35%, #a63a1c 65%, #5e1c12 100%); }
  .cover-3 { background: linear-gradient(180deg, #1d3042 0%, #2f4a5e 45%, #8a4a2a 80%, #c06a2c 100%); }
  .details { position: absolute; left: 111px; top: 23px; color: var(--accent); font-size: 13.5px; line-height: 23px; }
  .title { color: var(--accent-bright); font-weight: 400; font-size: 14px; }
  .buy { color: var(--accent); text-decoration: none; }
</style>
</head>
<body>
<div class="site">
  <header class="topbar">
    <div class="brand">Logo</div>
    <nav class="nav">
      <div class="nav-item nav-home">
        <svg viewBox="0 0 24 24"><path d="M10 20v-6h4v6h5v-8h3L12 3 2 12h3v8z"/></svg>Home
      </div>
      <div class="nav-item nav-novels">
        <svg viewBox="0 0 24 24"><path d="M18 2H6c-1.1 0-2 .9-2 2v16c0 1.1.9 2 2 2h12c1.1 0 2-.9 2-2V4c0-1.1-.9-2-2-2zM7 4h5v8l-2.5-1.5L7 12z"/></svg>Novels
      </div>
      <div class="nav-item nav-world">
        <svg viewBox="0 0 24 24"><path d="M12 2a10 10 0 1 0 0 20 10 10 0 0 0 0-20zm6.9 6h-2.9a15.7 15.7 0 0 0-1.4-3.6A8 8 0 0 1 18.9 8zM12 4c.8 1.2 1.5 2.5 1.9 4h-3.8c.4-1.4 1.1-2.8 1.9-4zM4.3 14a8.2 8.2 0 0 1 0-4h3.4a16 16 0 0 0 0 4zm.8 2h2.9c.3 1.3.8 2.5 1.4 3.6A8 8 0 0 1 5.1 16zM8 8H5.1a8 8 0 0 1 4.3-3.6C8.8 5.5 8.3 6.7 8 8zm4 12c-.8-1.2-1.5-2.5-1.9-4h3.8c-.4 1.4-1.1 2.8-1.9 4zm2.3-6H9.7a14.7 14.7 0 0 1 0-4h4.6a14.7 14.7 0 0 1 0 4zm.3 5.6c.6-1.1 1.1-2.3 1.4-3.6h2.9a8 8 0 0 1-4.3 3.6zm1.7-5.6a16 16 0 0 0 0-4h3.4a8.2 8.2 0 0 1 0 4z"/></svg>World
        <svg class="caret" viewBox="0 0 24 24"><path d="M5 8l7 8 7-8z"/></svg>
      </div>
      <div class="nav-item nav-author">
        <svg viewBox="0 0 24 24"><path d="M12 12a4 4 0 1 0 0-8 4 4 0 0 0 0 8zm0 2c-2.7 0-8 1.3-8 4v2h16v-2c0-2.7-5.3-4-8-4z"/></svg>Author
        <svg class="caret" viewBox="0 0 24 24"><path d="M5 8l7 8 7-8z"/></svg>
      </div>
    </nav>
  </header>

  <div class="search-label">Seacrh Book</div>
  <div class="search-rule"></div>

  <ul class="book-list">
    <li class="book">
      <div class="cover cover-1" role="img" aria-label="Cover art for The Scarlet Blade"></div>
      <div class="details">
        <div class="title">The Scarlet Blade</div>
        <div>Publisher: Halvern &amp; Lowe (Nox)</div>
        <div>Editor: Miriam Feld</div>
        <a class="buy" href="#">Buy Online</a>
      </div>
    </li>
    <li class="book">
      <div class="cover cover-2" role="img" aria-label="Cover art for The Onyx Seal"></div>
      <div class="details">
        <div class="title">The Onyx Seal</div>
        <div>Publisher: Halvern &amp; Lowe (Nox)</div>
        <div>Editor: Miriam Feld</div>
        <a class="buy" href="#">Buy Online</a>
      </div>
    </li>
    <li class="book">
      <div class="cover cover-3" role="img" aria-label="Cover art for The Hallowed Charm"></div>
      <div class="details">
        <div class="title">The Hallowed Charm</div>
        <div>Publisher: Halvern &amp; Lowe (Nox)</div>
        <div>Editor: Miriam Feld</div>
        <a class="buy" href="#">Buy Online</a>
      </div>
    </li>
  </ul>
</div>
</body>
</html>
```